Media Company's Events Website Needs a Design

International Media Company is setting up a new website to market own and partners' events in the Asia Pacific region.

The sitemap and sections are described in the attached document. Supporting images, logos and layout for the mockups are also provided.

We require design mockups for 4 key pages. Please submit homepage mockup for evaluation first. We will give the go-ahead for the other 3 pages once your homepage design is approved, so you do not have to waste unnecessary time.

Any question which I did not cover, please email milo+artpanel@brightvane.example. Thanks!
Updates

Hi all designers, our client has decided to simplify the website, dropping 2 event categories and focusing on just 1 (i.e. Vivid Pathways). 

I am uploading a new homepage layout doc. 

Specifically, changes are:
- New set of tabs on the main menu
- Content area will include: (i) testimonial slider; (ii) video block; (iii) list of upcoming events. feel free to play around with the layout.

Thanks and sorry for the trouble!
Milo

Hi all designers, I have re-uploaded the new brief with respect to the section changes.

Please download and refer to the changes.

Thanks!

Target Market(s)

Corporations, Businessmen, C-level Executives

Industry/Entity Type

Events

Requirements
Must have
• Refer to layout document
Nice to have
• The website may be implemented using WordPress, so a typical 1- and 2-column layout would be deployment-friendly.

```html
<!DOCTYPE html>
<html lang="en">
<head>
<meta charset="utf-8">
<title>Vivid Pathways – Events</title>
<link href="https://fonts.googleapis.com/css2?family=PT+Sans:ital,wght@0,400;0,700;1,400&display=swap" rel="stylesheet">
<style>
:root{
  --navy:#14226a;
  --navy-edge:#2b4ba6;
  --nav-active:#3d66b8;
  --link:#2b7bc0;
  --quote:#3b5fb2;
  --red:#e02219;
  --green:#8cc63e;
  --green-dark:#5d9a1e;
  --lime:#a6d84a;
  --grey-band:#f4f4f4;
  --text:#444;
  --footer:#2c2c2c;
  --footer-text:#cfcfcf;
}
*{box-sizing:border-box;margin:0;padding:0}
html,body{width:898px;height:1200px;overflow:hidden}
body{position:relative;background:#fff;font-family:"PT Sans",Arial,sans-serif;color:var(--text)}
.abs{position:absolute}
a{text-decoration:none;color:inherit}

.brand{left:107px;top:26px;font-size:27px;color:#555;letter-spacing:-.5px}
.top-links{right:97px;top:11px;font-size:10px;color:var(--link)}
.top-links span{color:#999;margin:0 4px}
.section-title{right:97px;top:47px;font-size:18px;font-weight:700;color:#777;letter-spacing:1px}

.main-nav{left:0;top:86px;width:898px;height:32px;background:linear-gradient(#223a8f,#13236c)}
.main-nav ul{list-style:none;position:absolute;left:90px;top:0;display:flex;height:32px}
.main-nav li{color:#fff;font-size:11.5px;line-height:32px;padding:0 8px;border-right:1px solid #2e4a9e}
.main-nav li:last-child{border-right:0}
.main-nav li.active{background:var(--nav-active);padding:0 11px}

.hero{left:0;top:118px;width:898px;height:305px;background:var(--grey-band)}
.arrow{top:140px}
.speaker-photo{left:123px;top:39px;width:228px;height:237px;border:3px solid #fff;box-shadow:0 1px 4px rgba(0,0,0,.35);background:linear-gradient(135deg,#6b5236,#2f2520 60%,#4b3b2c)}
.quote{left:371px;top:60px;width:430px;font-size:16px;line-height:25px;color:var(--quote)}
.quote .mark{color:#9aa;font-size:20px;font-weight:700}
.speaker{left:371px;top:185px;font-size:13.5px;line-height:22px;color:#555}
.speaker .org{color:var(--red)}
.watch{left:371px;top:244px;font-size:19px;color:var(--red);display:flex;align-items:center;gap:8px}

.video{left:100px;top:455px;width:372px;height:222px;border:3px solid #fff;box-shadow:0 0 3px rgba(0,0,0,.35);background:linear-gradient(120deg,#7d7f8a,#b23b3c 45%,#5a6070);overflow:hidden}
.video .caption{position:absolute;left:0;bottom:0;width:100%;height:57px;background:rgba(25,25,25,.75);padding:12px 25px;font-size:12px;color:#fff;line-height:17px}
.video .caption em{font-style:normal;color:#f2a81d}
.play{left:165px;top:55px}

.events-title{left:100px;top:703px;font-size:17px;color:var(--navy)}
.event-card{left:97px;width:286px;height:86px;border:1px solid #ddd;border-radius:3px;background:linear-gradient(#fff,#ececec)}
.event-card .name{position:absolute;left:11px;top:24px;width:140px;font-size:15px;font-weight:700;line-height:16px;color:#1d6f86}
.event-card .info{position:absolute;left:163px;top:14px;font-size:12.5px;line-height:17px;color:#444;font-weight:700}
.event-card .info a{display:block;margin-top:5px;font-size:9.5px;color:var(--link);font-weight:400}
.calendar-btn{left:283px;top:931px;width:99px;height:28px;border:1px solid var(--green-dark);border-radius:3px;background:linear-gradient(#a0d352,#7cb92f);color:#1b3b06;font-size:11.5px;text-align:center;line-height:26px}

.conversations{left:500px;top:455px;width:301px;height:525px;background:var(--navy);border:2px solid var(--navy-edge);color:#fff;text-align:center}
.conversations h2{position:absolute;top:17px;width:100%;font-size:20px;font-weight:700}
.conversations .rule{position:absolute;left:10px;width:277px;height:1px;background:#5b6aa6}
.conversations h3{position:absolute;width:100%;font-size:16.5px;font-weight:400}
.conversations p{position:absolute;left:24px;width:250px;font-size:10.5px;font-style:italic;line-height:17px;color:#c7cbe0;text-align:justify}
.conversations .center{text-align:center}
.conversations .by{position:absolute;right:22px;font-size:11.5px;font-weight:700;color:var(--lime)}
.conversations .more{position:absolute;top:488px;width:100%;font-size:11.5px;font-weight:700;color:#dde}

.footer{left:0;top:1009px;width:898px;height:191px;background:var(--footer);color:var(--footer-text)}
.footer ul{list-style:none;position:absolute;font-size:9px;line-height:17px}
.footer li::before{content:"›";color:#7cb92f;margin-right:12px}
.footer h4{position:absolute;font-size:12px;font-weight:700;color:#fff}
.social{position:absolute;left:410px;top:40px;font-size:9.5px;line-height:22px}
.social div{display:flex;align-items:center;gap:10px}
.social i{display:inline-block;width:16px;height:16px;border-radius:3px}
.news-input{position:absolute;left:545px;top:41px;width:181px;height:21px;border:1px solid #555;border-radius:3px;background:#444;font-size:9px;font-style:italic;color:#aaa;padding:4px 9px}
.subscribe{position:absolute;left:741px;top:41px;width:60px;height:20px;border-radius:2px;background:var(--green);color:#1b3b06;font-size:11px;text-align:center;line-height:20px}
.footer .brand-small{position:absolute;left:575px;top:95px;font-size:20px;color:#ccc}
.copyright{position:absolute;left:575px;top:132px;font-size:8.5px;line-height:15px;color:#aaa}
</style>
</head>
<body>

<header>
  <div class="abs brand">Vivid Pathways</div>
  <div class="abs top-links">Login<span>|</span>Register<span>|</span>Newsletter Signup<span>|</span>Contact Us<span>|</span>Site Map</div>
  <div class="abs section-title">EVENTS</div>
  <nav class="abs main-nav">
    <ul>
      <li class="active">Home</li><li>About Vivid Pathways</li><li>Upcoming Events</li><li>Past Events</li><li>Partnership Opportunities</li><li>Videos</li><li>Conversations</li><li>Calendar</li>
    </ul>
  </nav>
</header>

<section class="abs hero">
  <svg class="abs arrow" style="left:90px" width="18" height="30" viewBox="0 0 18 30"><polyline points="15,2 3,15 15,28" fill="none" stroke="#aaa" stroke-width="3"/></svg>
  <svg class="abs arrow" style="left:790px" width="18" height="30" viewBox="0 0 18 30"><polyline points="3,2 15,15 3,28" fill="none" stroke="#aaa" stroke-width="3"/></svg>
  <div class="abs speaker-photo" role="img" aria-label="Photo of a speaker in a suit holding a microphone"></div>
  <blockquote class="abs quote"><span class="mark">“</span> What’s great about Hangzhou and having officials from the city come to San Francisco to share their ideas, we learn a lot about IP protection, about their real investment in making it a really clean and global city...... <span class="mark">”</span></blockquote>
  <div class="abs speaker">Daniel Reyes, Chief Commercial Officer,<br><span class="org">Brightfield Solar</span></div>
  <a class="abs watch">Watch Video
    <svg width="17" height="17" viewBox="0 0 17 17"><rect width="17" height="17" rx="2" fill="#e02219"/><polygon points="6,4 13,8.5 6,13" fill="#fff"/></svg></a>
</section>

<div class="abs video" role="img" aria-label="Video still of a panel discussion on stage">
  <svg class="abs play" width="66" height="66" viewBox="0 0 66 66"><circle cx="33" cy="33" r="31" fill="rgba(255,255,255,.45)"/><polygon points="25,18 48,33 25,48" fill="rgba(90,90,90,.7)"/></svg>
  <div class="caption"><em>Watch Video</em><br>Sir Alan Whitcombe, President of Aerolux UK</div>
</div>

<h2 class="abs events-title">Upcoming Events</h2>
<div class="abs event-card" style="top:736px">
  <div class="name">FUTURE FORUM ASIA</div>
  <div class="info">September 12 2012<br>Tianjin, China<a>Find More</a></div>
</div>
<div class="abs event-card" style="top:835px">
  <div class="name" style="top:32px;color:#8a1d4a">ENERGY SUMMIT ASIA</div>
  <div class="info">October 3 - 5 2012<br>Bangkok, Thailand<a>Find More</a></div>
</div>
<a class="abs calendar-btn">See Full Calendar</a>

<aside class="abs conversations">
  <h2>Conversations</h2>
  <div class="rule" style="top:57px"></div>
  <h3 style="top:86px">Join the Brainstorm</h3>
  <p class="center" style="top:119px">What device will overtake tablets?</p>
  <h3 style="top:177px">Discussions</h3>
  <p style="top:213px">Duis aute irure dolor in reprehenderit in voluptate velit esse cillum dolore eu fugiat nulla pariatur. Excepteur sint occaecat.</p>
  <h3 style="top:313px">Ask a Question</h3>
  <p style="top:348px;left:22px;width:256px">Duis aute irure dolor in reprehenderit in voluptate velit esse cillum dolore eu fugiat nulla pariatur. Excepteur sint occaecat.</p>
  <div class="by" style="top:401px">- Grace Lim,&nbsp; TL &amp; Co.</div>
  <div class="rule" style="top:461px"></div>
  <div class="more">See more Converations &nbsp;»</div>
</aside>

<footer class="abs footer">
  <ul style="left:99px;top:22px">
    <li>Home</li><li>About Vivid Pathways</li><li>Upcoming Events</li><li>Past Events</li><li>Partner Events</li><li>Videos</li><li>Sponsorship</li><li>Calendar</li>
  </ul>
  <ul style="left:263px;top:22px">
    <li>Login</li><li>Register</li><li>Newsletter Signup</li><li>Contact Us</li>
  </ul>
  <h4 style="left:410px;top:18px">Connect Us</h4>
  <div class="social">
    <div><i style="background:#3b5a9a"></i>Friendbook</div>
    <div><i style="background:#39a7d6"></i>Chirper</div>
    <div><i style="background:#1f73a8"></i>ProLink</div>
    <div><i style="background:#222;border:1px solid #666"></i>Circles +</div>
    <div><i style="background:#c92b25"></i>TubeCast</div>
    <div><i style="background:#f08a24"></i>Rss Feed</div>
  </div>
  <h4 style="left:547px;top:18px">Newletter Sign Up</h4>
  <div class="news-input">enter email address</div>
  <div class="subscribe">Subscribe</div>
  <div class="brand-small">Vivid Pathways</div>
  <div class="copyright">Copyright © 2012 vividpathways.example.<br>All Right Reserved &nbsp;|&nbsp; Privacy Policy</div>
</footer>

</body>
</html>
```